Business Card Design Project

Use our current logo. Clean design.

Industry/Entity Type

Business

Requirements
Must have
• Marisela DUBRANCQ
M. Law
Managing Partner

Alpenvorsa AG
Kornhalmweg 214
CH-3097 Liebefeld

M. +41 79 412 56 27
T. +41 31 928 44 10
F. +41 31 928 44 19

m.dubrancq@alpenvorsa-example.com
www.alpenvorsa-example.com

```html
<!DOCTYPE html>
<html lang="de">
<head>
<meta charset="utf-8">
<title>Alpenvorsa AG – Visitenkarte</title>
<link rel="stylesheet" href="https://fonts.googleapis.com/css2?family=PT+Sans+Narrow&family=Marcellus&display=swap">
<style>
  :root {
    --backdrop: #dcdad6;
    --card: #f1f1f0;
    --ink: #1f1f1f;
    --ink-soft: #3a3a3a;
    --accent: #c8473f;
    --shadow: rgba(0, 0, 0, 0.18);
  }
  * { box-sizing: border-box; margin: 0; padding: 0; }
  html, body {
    width: 1200px;
    height: 900px;
    overflow: hidden;
    background: var(--backdrop);
  }
  .canvas {
    position: relative;
    width: 1200px;
    height: 900px;
  }
  .card {
    position: absolute;
    left: 340px;
    width: 520px;
    height: 300px;
    background: var(--card);
    box-shadow: 0 6px 18px var(--shadow), 0 1px 2px var(--shadow);
    color: var(--ink);
    font-family: "PT Sans Narrow", "Arial Narrow", sans-serif;
  }
  .card--back { top: 120px; }
  .card--front { top: 480px; }

  /* Back side */
  .brand-line {
    position: absolute;
    right: 40px;
    top: 112px;
    text-align: right;
  }
  .brand-line__name {
    font-family: "Marcellus", serif;
    font-size: 30px;
    letter-spacing: 1.5px;
    color: var(--ink);
    line-height: 1;
    padding: 0 2px 7px 0;
  }
  .brand-line__rule {
    height: 1px;
    background: var(--accent);
    width: 250px;
    margin-left: auto;
  }
  .brand-line__web {
    font-size: 14px;
    letter-spacing: 3.2px;
    color: var(--ink-soft);
    padding-top: 8px;
  }

  /* Front side */
  .company-address {
    position: absolute;
    left: 300px;
    top: 34px;
    font-size: 13px;
    line-height: 16px;
    color: var(--ink-soft);
  }
  .company-address .name { text-transform: uppercase; letter-spacing: 0.3px; }
  .company-address .phones { margin-top: 10px; padding-left: 18px; }
  .company-address .phones span { display: inline-block; width: 14px; }

  .person {
    position: absolute;
    left: 300px;
    top: 160px;
    padding-left: 22px;
    border-left: 1px solid var(--accent);
    padding-top: 4px;
    padding-bottom: 4px;
  }
  .person__name {
    font-size: 21px;
    line-height: 24px;
    color: var(--ink);
  }
  .person__details {
    font-size: 13px;
    line-height: 17px;
    color: var(--ink-soft);
    margin-top: 2px;
  }

  .company-name {
    position: absolute;
    left: 42px;
    bottom: 56px;
    display: flex;
    align-items: center;
    gap: 10px;
    font-family: "PT Sans Narrow", "Arial Narrow", sans-serif;
    font-size: 26px;
    letter-spacing: 1px;
    color: var(--ink);
    text-transform: uppercase;
  }
  .company-name__mark {
    width: 14px;
    height: 14px;
    background: var(--ink);
  }
</style>
</head>
<body>
<main class="canvas">
  <section class="card card--back" aria-label="Kartenrückseite">
    <div class="brand-line">
      <div class="brand-line__name">ALPENVORSA</div>
      <div class="brand-line__rule"></div>
      <div class="brand-line__web">www.alpenvorsa-example.com</div>
    </div>
  </section>

  <section class="card card--front" aria-label="Kartenvorderseite">
    <div class="company-address">
      <div class="name">Alpenvorsa AG</div>
      <div>Kornhalmweg 214</div>
      <div>CH-3097 Liebefeld</div>
      <div class="phones">
        <div><span>T</span>+41 31 928 44 10</div>
        <div><span>F</span>+41 31 928 44 19</div>
      </div>
    </div>

    <div class="person">
      <div class="person__name">Marisela DUBRANCQ</div>
      <div class="person__details">
        <div>M. Law | Managing Partner</div>
        <div>+41 79 412 56 27</div>
        <div>m.dubrancq@alpenvorsa-example.com</div>
      </div>
    </div>

    <div class="company-name">
      <span class="company-name__mark" aria-hidden="true"></span>
      <span>Alpenvorsa</span>
    </div>
  </section>
</main>
</body>
</html>
```